Voucher design

Design of vouchers with logo etc.
There must be a name field and a coupon code field.
The vouchers must be suitable for printing and digital delivery.
There must be a voucher on the voucher and the berag must be replaceable by us
our website www.kolbo-rixe.eu

Industry/Entity Type

Kolbo Rix Fachgescäft

Requirements
Must have
• There must be a voucher on the voucher and the berag must be replaceable by us

```html
<!DOCTYPE html>
<html lang="en">
<head>
<meta charset="utf-8">
<title>Kolbo Rix Discount Voucher</title>
<link rel="stylesheet" href="https://fonts.googleapis.com/css2?family=Bebas+Neue&family=Josefin+Sans:wght@400&family=Quicksand:wght@600&family=Exo+2:ital,wght@0,500;1,700&display=swap">
<style>
  :root {
    --backdrop: #efeeec;
    --band: #ebebef;
    --band-line: #d6d6dc;
    --yellow: #fecd0a;
    --ink: #1f1b1c;
    --white: #ffffff;
    --badge-dark: #2b2417;
  }
  * { margin: 0; padding: 0; box-sizing: border-box; }
  html, body { width: 1200px; height: 1200px; overflow: hidden; background: var(--backdrop); }
  .voucher {
    position: absolute; left: 114px; top: 401px; width: 972px; height: 398px;
    box-shadow: 0 8px 22px rgba(0,0,0,0.18);
    overflow: hidden;
  }
  .voucher-header {
    position: absolute; left: 0; top: 0; width: 100%; height: 135px;
    background: linear-gradient(180deg, #eeeef2, var(--band));
  }
  .brand {
    position: absolute; left: 47px; top: 47px;
    display: flex; align-items: center; gap: 10px;
    font-family: "Exo 2", sans-serif; font-weight: 500; font-size: 34px;
    color: var(--ink); letter-spacing: 0.5px;
  }
  .brand-dot { width: 14px; height: 14px; border-radius: 50%; background: var(--yellow); }
  .website {
    position: absolute; right: 48px; top: 64px;
    font-family: "Exo 2", sans-serif; font-weight: 500; font-size: 15px;
    color: var(--ink); letter-spacing: 0.6px;
  }
  .website-rules {
    position: absolute; right: 0; top: 72px; width: 39px;
  }
  .website-rules span { display: block; height: 1.5px; background: var(--ink); margin-bottom: 3px; }
  .voucher-body {
    position: absolute; left: 0; top: 135px; width: 100%; height: 263px;
    background: var(--yellow);
  }
  .title { position: absolute; left: 47px; top: 41px; width: 373px; }
  .title-main {
    font-family: "Bebas Neue", sans-serif; font-size: 146px; line-height: 112px;
    color: var(--ink); letter-spacing: 0; white-space: nowrap;
    display: block; height: 112px;
    transform: scaleX(0.855); transform-origin: left center;
  }
  .title-rule { height: 1.5px; background: var(--ink); }
  .title-sub {
    font-family: "Josefin Sans", sans-serif; font-size: 68px; line-height: 66px;
    color: var(--ink); letter-spacing: 3.5px; padding-top: 6px; height: 66px;
    display: block; white-space: nowrap;
  }
  .field { position: absolute; left: 474px; width: 217px; }
  .field-name { top: 38px; }
  .field-code { top: 150px; }
  .field-label {
    font-family: "Quicksand", sans-serif; font-weight: 600; font-size: 21px;
    color: var(--ink); display: block; height: 32px;
  }
  .field-input { height: 32px; background: var(--white); }
  .spotlight-art {
    position: absolute; left: 700px; top: 0; width: 272px; height: 263px;
    background:
      radial-gradient(ellipse 60px 140px at 250px 40px, rgba(255,245,150,0.55), transparent 70%),
      radial-gradient(ellipse 40px 140px at 60px 60px, rgba(255,245,150,0.5), transparent 70%),
      radial-gradient(ellipse 90px 10px at 150px 245px, rgba(160,120,0,0.35), transparent 80%);
  }
  .lamp-arm {
    position: absolute; left: 809px; top: 0; width: 49px; height: 75px;
    background: linear-gradient(180deg, #1c1a16, #3a3220);
  }
  .badge { position: absolute; left: 751px; top: 68px; width: 170px; height: 170px; }
</style>
</head>
<body>
  <main class="voucher">
    <header class="voucher-header" role="img" aria-label="Light grey band with a fine wavy line pattern">
      <div class="brand"><span class="brand-dot"></span>Kolbo-Rixe.eu</div>
      <div class="website">www.kolbo-rixe.eu</div>
      <div class="website-rules"><span></span><span></span><span></span></div>
    </header>
    <section class="voucher-body">
      <div class="title">
        <span class="title-main">DISCOUNT</span>
        <div class="title-rule"></div>
        <span class="title-sub">VOUCHER</span>
        <div class="title-rule"></div>
      </div>
      <div class="field field-name">
        <span class="field-label">Name</span>
        <div class="field-input"></div>
      </div>
      <div class="field field-code">
        <span class="field-label">Coupon Code</span>
        <div class="field-input"></div>
      </div>
      <div class="spotlight-art" role="img" aria-label="Golden stage spotlights shining down with sparkling light"></div>
      <div class="lamp-arm"></div>
      <svg class="badge" viewBox="0 0 170 170" aria-label="50% discount">
        <defs>
          <radialGradient id="badgeFill" cx="50%" cy="40%" r="60%">
            <stop offset="0%" stop-color="#6b5620"/>
            <stop offset="100%" stop-color="#201c15"/>
          </radialGradient>
        </defs>
        <circle cx="85" cy="85" r="83" fill="var(--yellow)" stroke="var(--ink)" stroke-width="2"/>
        <circle cx="85" cy="85" r="77" fill="url(#badgeFill)"/>
        <text x="80" y="112" text-anchor="middle" font-family="Quicksand, sans-serif" font-weight="600"
              font-size="72" fill="var(--yellow)" stroke="var(--white)" stroke-width="3" paint-order="stroke">50</text>
        <text x="132" y="70" text-anchor="middle" font-family="Quicksand, sans-serif" font-weight="600"
              font-size="22" fill="var(--yellow)" stroke="var(--white)" stroke-width="2" paint-order="stroke">%</text>
      </svg>
    </section>
  </main>
</body>
</html>
```